Geschäftspapier für Pfandhaus und Juwelier gesucht
Zielgruppe
Pfandhaus und Juwelier.
Aufgabenstellung
Ich betreibe mehrere Filialen und möchte all diese wir einem Briefkopf haben und ggf Platz für weitere da ich gerade 2 weitere eröffne. Unter www.leihhaus-Borlen.de sieht man Logo und Farben.
Ich möchte das Briefpapier als Datei haben und nicht gedruckt sondern will es selbst am Firmendrucker drucken.Die Bankverbindung sollte auch darauf sein aber erstmal etwas am Platzhalter eintragen .

```html
<!DOCTYPE html>
<html lang="de">
<head>
<meta charset="utf-8">
<title>Briefpapier Matthias Borlen Leihhaus</title>
<link href="https://fonts.googleapis.com/css2?family=Open+Sans:wght@400;600&display=swap" rel="stylesheet">
<style>
:root{
  --gold:#b39b63;
  --charcoal:#4a4949;
  --ink:#1d1d1d;
  --paper:#ffffff;
  --backdrop:#e9e9ea;
  --rule:#c9b78e;
}
*{box-sizing:border-box;margin:0;padding:0}
html,body{width:1200px;height:1010px;overflow:hidden;background:var(--backdrop)}
body{font-family:"Open Sans",Arial,sans-serif;color:var(--ink)}
.sheet{position:absolute;left:255px;top:12px;width:690px;height:986px;background:var(--paper);box-shadow:0 2px 10px rgba(0,0,0,.12);overflow:hidden}
.top-rule{position:absolute;left:0;top:10px;width:430px;height:4px;background:var(--gold)}
.brand-box{position:absolute;left:430px;top:10px;width:205px;height:118px;background:var(--charcoal);display:flex;flex-direction:column;align-items:center;justify-content:center}
.brand-name{color:var(--gold);font-weight:400;font-size:21px;line-height:1.25;text-align:center}
.sender-line{position:absolute;left:62px;top:222px;font-size:7.5px;text-decoration:underline;letter-spacing:.1px}
.recipient{position:absolute;left:62px;top:242px;font-size:11.5px;line-height:1.35}
.fold-mark{position:absolute;left:0;width:18px;height:1px;background:#b8b8b8}
.fold-mark.upper{top:348px}
.fold-mark.lower{top:695px}
.branches{position:absolute;left:40px;right:20px;bottom:48px;display:flex}
.branch{width:126px;padding:0 8px;border-left:1px solid var(--rule);font-size:8.2px;line-height:1.45}
.branch:first-child{border-left:none;padding-left:0}
.branch .line{display:flex;align-items:center;gap:5px}
.branch svg{width:8px;height:8px;flex:none}
.footer-band{position:absolute;left:0;bottom:0;width:690px;height:42px}
.bank-info{position:absolute;left:60px;bottom:4px;display:flex;color:#fff;font-size:9.5px;line-height:1.3}
.bank-info div{padding:0 14px;border-left:1px solid rgba(255,255,255,.7)}
.bank-info div:first-child{border-left:none;padding-left:0}
.web{position:absolute;right:48px;bottom:9px;color:#fff;font-size:11px}
</style>
</head>
<body>
<div class="sheet">
  <div class="top-rule"></div>
  <div class="brand-box">
    <span class="brand-name">Matthias Borlen<br>Leihhaus</span>
  </div>

  <p class="sender-line">Matthias Borlen Leihhaus | Lindenhofstraße 4 | 66111 Saarbrücken</p>
  <address class="recipient" style="font-style:normal">Herr<br>Mark Mustermann<br>Musterweg 13<br>24102 Dortmund</address>

  <span class="fold-mark upper"></span>
  <span class="fold-mark lower"></span>

  <svg width="0" height="0" style="position:absolute">
    <defs>
      <symbol id="icon-phone" viewBox="0 0 10 10"><path d="M2 1l2 2-1 1.2c.6 1.2 1.5 2.1 2.7 2.7L7 6l2 2-1.2 1.2C4.5 9 1 5.5.8 2.2z" fill="#b39b63"/></symbol>
      <symbol id="icon-fax" viewBox="0 0 10 10"><rect x="2.5" y="1" width="5" height="3" fill="#b39b63"/><rect x="1" y="4" width="8" height="3.5" rx=".6" fill="#b39b63"/><rect x="2.5" y="6.5" width="5" height="2.5" fill="#b39b63"/></symbol>
      <symbol id="icon-mail" viewBox="0 0 10 10"><rect x="1" y="2" width="8" height="6" fill="#b39b63"/><path d="M1 2l4 3.2L9 2" stroke="#fff" stroke-width=".8" fill="none"/></symbol>
    </defs>
  </svg>

  <div class="branches">
    <div class="branch">Lindenhofstraße 4<br>66111 Saarbrücken
      <div class="line"><svg><use href="#icon-phone"/></svg>+49 (0) 681 4410277-0</div>
      <div class="line"><svg><use href="#icon-fax"/></svg>+49 (0) 681 4410277-9</div>
      <div class="line"><svg><use href="#icon-mail"/></svg>sb@leihhaus-borlen.de</div>
    </div>
    <div class="branch">Kastanienweg 7<br>54290 Trier
      <div class="line"><svg><use href="#icon-phone"/></svg>+49 (0) 651 3307462-5</div>
      <div class="line"><svg><use href="#icon-fax"/></svg>+49 (0) 651 3307462-0</div>
      <div class="line"><svg><use href="#icon-mail"/></svg>tr@leihhaus-borlen.de</div>
    </div>
    <div class="branch">Ulmenallee 22<br>55116 Mainz
      <div class="line"><svg><use href="#icon-phone"/></svg>+49 (0) 6131 5173040</div>
      <div class="line"><svg><use href="#icon-fax"/></svg>+49 (0) 6131 5173048</div>
      <div class="line"><svg><use href="#icon-mail"/></svg>mz@leihhaus-borlen.de</div>
    </div>
    <div class="branch">Birkenstraße 51<br>65185 Wiesbaden
      <div class="line"><svg><use href="#icon-phone"/></svg>+49 (0) 611 72638415</div>
      <div class="line"><svg><use href="#icon-fax"/></svg>+49 (0) 611 72638419</div>
      <div class="line"><svg><use href="#icon-mail"/></svg>wi@leihhaus-borlen.de</div>
    </div>
    <div class="branch">Eichengasse 3<br>67655 Kaiserslautern
      <div class="line"><svg><use href="#icon-phone"/></svg>+49 (0) 0631 38275</div>
      <div class="line"><svg><use href="#icon-mail"/></svg>kl@leihhaus-borlen.de</div>
    </div>
  </div>

  <svg class="footer-band" viewBox="0 0 690 42" preserveAspectRatio="none">
    <polygon points="0,14 492,14 482,42 0,42" fill="var(--gold)"/>
    <polygon points="498,0 656,0 640,42 482,42" fill="var(--charcoal)"/>
    <polygon points="664,0 690,0 690,30 654,30" fill="var(--gold)"/>
  </svg>
  <div class="bank-info">
    <div>Bankverbindung:<br>Matthias Borlen</div>
    <div>Rheinland Bank<br>USt-ID-Nr. DEXXXXXXXX</div>
    <div>IBAN: DEXX XXXX XXXX XXXX XXXX X<br>BIC: XXXXXXXX</div>
  </div>
  <span class="web">www.leihhaus-Borlen.de</span>
</div>
</body>
</html>
```